Brill Insurance Agency - Business Cards

Hello, I am needing new trendy business cards for our Insurance Agency now that I have a new Logo. I have attached our new logo with several color options along with a business card design that I like. I am leaning towards burgundy and blue colors. I have attached our current business card. I have also attached a headshot of our company president, Martin Vale, that you can use if you wish. Thank you so much in advance for all the wonderful designs!!!!

Target Market(s)

We want to look very professional to potential customers and we also want to look very professional so insurance companies will want to contract with us to sell their product.

Industry/Entity Type

Insurance

Contact Information for Business Card

Martin Vale
mvale@brillagency.com
Business: 555-213-4087
Fax: 555-213-7751
Cell: 555-390-2618
Toll Free: 888-555-0194
42 W Elm Rd Larkfield, MO 64011
www.brillagency.net

Font styles to use
Serif
Sans Serif

Colors
0355a3
3277b5
f04a50
ec1f27

Requirements
Nice to have
• I love creativity. The more creative and balanced a business card design the more I will like it. I would like the card to be printed horizontally instead of vertically.
Should not have
• My project should not have the Allied Coverage Network logo. It is no longer used in the industry.

```html
<!DOCTYPE html>
<html lang="en">
<head>
<meta charset="utf-8">
<title>Brill Insurance Agency – Business Cards</title>
<link rel="stylesheet" href="https://fonts.googleapis.com/css2?family=Arimo:wght@400;700&family=Montserrat:wght@600&display=swap">
<style>
  :root {
    --brand-blue: #0b55a3;
    --brand-red: #f04a50;
    --ink: #3d3d3d;
    --rule: #555555;
    --paper: #ffffff;
    --stage: #e9e7e3;
    --faint: #eef1f6;
  }
  * { box-sizing: border-box; margin: 0; padding: 0; }
  html, body { width: 900px; height: 1200px; overflow: hidden; }
  body { background: var(--stage); font-family: "Arimo", Arial, sans-serif; position: relative; }

  .card {
    position: absolute; left: 87px; width: 735px; height: 428px;
    border-radius: 22px; overflow: hidden;
    box-shadow: 0 6px 14px rgba(0,0,0,.25);
  }
  .card--front { top: 137px; background: var(--paper); }
  .card--back { top: 634px; background: var(--brand-blue); }

  .abs { position: absolute; }

  /* front */
  .faint-ring { right: -50px; top: -20px; width: 280px; height: 280px; border: 44px solid var(--faint); border-radius: 50%; }
  .brand-dot { left: 27px; top: 37px; width: 96px; height: 96px; border: 12px solid var(--brand-blue); border-radius: 50%; }
  .divider { left: 158px; width: 3px; background: var(--rule); }
  .divider--brand { top: 28px; height: 112px; }
  .divider--name { top: 199px; height: 47px; width: 2px; }
  .divider--contact { top: 288px; height: 106px; width: 2px; }
  .wordmark { left: 175px; top: 58px; font-family: "Montserrat", sans-serif; font-weight: 600; color: var(--brand-blue); line-height: 1; }
  .wordmark__main { font-size: 31px; display: block; letter-spacing: -0.3px; }
  .wordmark__sub { font-size: 19px; letter-spacing: 5px; display: block; margin-top: 8px; }

  .person { left: 177px; top: 198px; }
  .person__name { font-size: 28px; font-weight: 700; color: var(--brand-blue); }
  .person__title { font-size: 16px; color: var(--ink); margin-top: 4px; }

  .contact-list { left: 177px; top: 286px; list-style: none; }
  .contact-list li { height: 22.5px; display: flex; align-items: center; font-size: 17px; color: var(--ink); }
  .contact-list svg { width: 13px; height: 13px; margin-right: 11px; fill: var(--brand-red); }
  .accent { color: var(--brand-red); }

  .address { right: 26px; top: 286px; text-align: right; font-size: 17px; color: var(--ink); line-height: 21px; font-style: normal; }
  .toll-free { right: 26px; top: 375px; font-size: 17px; color: var(--ink); display: flex; align-items: center; }
  .toll-free svg { width: 16px; height: 14px; margin-right: 9px; fill: var(--brand-blue); }

  .band { left: 0; bottom: 0; width: 100%; height: 13px; }

  /* back */
  .back-mark { left: 312px; top: 118px; width: 110px; height: 110px; border: 13px solid #fff; border-radius: 50%; }
  .back-wordmark { left: 0; width: 100%; top: 254px; text-align: center; color: #fff; font-family: "Montserrat", sans-serif; font-weight: 600; line-height: 1; }
  .back-wordmark__main { font-size: 40px; display: block; }
  .back-wordmark__sub { font-size: 24px; letter-spacing: 6px; display: block; margin-top: 10px; }
  .services { left: 0; width: 100%; top: 386px; display: flex; justify-content: center; gap: 12px; color: #fff; font-size: 18px; letter-spacing: 1px; }
</style>
</head>
<body>

<section class="card card--front" aria-label="Business card front">
  <div class="abs faint-ring"></div>
  <div class="abs brand-dot"></div>
  <div class="abs divider divider--brand"></div>
  <div class="abs wordmark">
    <span class="wordmark__main">BRILL INSURANCE</span>
    <span class="wordmark__sub">AGENCY</span>
  </div>

  <div class="abs divider divider--name"></div>
  <div class="abs person">
    <p class="person__name">Martin Vale</p>
    <p class="person__title">President</p>
  </div>

  <div class="abs divider divider--contact"></div>
  <ul class="abs contact-list">
    <li><svg viewBox="0 0 12 12"><path d="M3 0h6a1 1 0 0 1 1 1v10a1 1 0 0 1-1 1H3a1 1 0 0 1-1-1V1a1 1 0 0 1 1-1zm0 1.5v7.5h6V1.5z"/></svg>555-213-4087</li>
    <li><svg viewBox="0 0 12 12"><path d="M2.5 0.5l2 2.2-1 1.3c.8 1.7 2 2.9 3.6 3.6l1.3-1 2.2 2-1.2 2.2C5 10.3 1.7 7 .4 1.7z"/></svg>555-213-4087</li>
    <li><svg viewBox="0 0 12 12"><path d="M3 0h5l1 1v3H3zM1 4.5h10a1 1 0 0 1 1 1V9H9.5v3h-7V9H0V5.5a1 1 0 0 1 1-1zm3 5v1.5h4V9.5z"/></svg>555-213-7751</li>
    <li><svg viewBox="0 0 12 12"><path d="M0 2h12v1.2L6 7 0 3.2zm0 2.6L6 8.4l6-3.8V10H0z"/></svg>mvale@<span class="accent">brillagency</span>.com</li>
    <li><svg viewBox="0 0 12 12"><path d="M6 0a6 6 0 1 0 0 12A6 6 0 0 0 6 0zm0 1c.7.8 1.2 2.2 1.3 4H4.7C4.8 3.2 5.3 1.8 6 1zM1 5h2.7c0 .3 0 .7 0 1s0 .7 0 1H1.1a5 5 0 0 1 0-2zm3.7 0h2.6v2H4.7zm3.6 0H11a5 5 0 0 1 0 2H8.3zM4.7 8h2.6C7.2 9.8 6.7 11.2 6 12c-.7-.8-1.2-2.2-1.3-4z"/></svg>www.<span class="accent">brillagency</span>.net</li>
  </ul>

  <address class="abs address">42 W Elm Rd Larkfield<br>MO 64011</address>
  <p class="abs toll-free"><svg viewBox="0 0 16 14"><path d="M1 4c0-2 3-3.5 7-3.5S15 2 15 4v1.5h-3.5V4H4.5v1.5H1zm3 2h8l3 3.5V13H1V9.5zm4 1.5a2 2 0 1 0 0 4 2 2 0 0 0 0-4z"/></svg>888-555-0194 (<span class="accent">Toll Free</span>)</p>

  <svg class="abs band" viewBox="0 0 735 13" preserveAspectRatio="none">
    <polygon points="0,0 465,0 452,13 0,13" fill="#0b55a3"/>
    <polygon points="472,0 735,0 735,13 459,13" fill="#f04a50"/>
  </svg>
</section>

<section class="card card--back" aria-label="Business card back">
  <div class="abs back-mark"></div>
  <div class="abs back-wordmark">
    <span class="back-wordmark__main">BRILL INSURANCE</span>
    <span class="back-wordmark__sub">AGENCY</span>
  </div>
  <p class="abs services"><span>Commercial</span><span>I</span><span>Home</span><span>I</span><span>Auto</span><span>I</span><span>Farm</span><span>I</span><span>Life</span><span>I</span><span>Health</span></p>
</section>

</body>
</html>
```